Retail swing tag labels for a sale / reduction

We need some graphics done to be made into retail swing tag labels, for the purpose of reductions on selected products.

We have attached 2 examples of previous designs that were similar idea, but more themed for 'autumn' and 'winter'. This theme will just have the word 'REDUCED'.

The white areas can be smaller in size, as we would like to include a large "20% OFF" at the bottom, and then a 30%, 40%, 50% option.

Overall colour scheme should be red background with some form of detailed patterning (see previous examples). Bright and e-catching.

Any other questions, just ask.

The screenshot is front the printers, but in horizontal orientation.

The finished dimensions will be A6 portrait, printed both sides.

We have also included the vector file of the shop "Hollowbrook Emporium", which can be included on 1 of the sides.

```html
<!DOCTYPE html>
<html lang="en">
<head>
<meta charset="utf-8">
<title>Reduced 20% Off – Hollowbrook Emporium</title>
<link rel="stylesheet" href="https://fonts.googleapis.com/css2?family=Anton&family=Oswald:wght@700&family=Montserrat:wght@400;700&display=swap">
<style>
  :root {
    --tag-red: #c0142a;
    --tag-red-deep: #a80f22;
    --ring-red: #e01f2a;
    --ring-red-dark: #7f1f2c;
    --figure-red: #d8192f;
    --white: #ffffff;
    --disc-shade: #c7ccc8;
    --frame-blue: #3a4ea3;
    --frame-green: #2d9a4a;
  }
  html, body {
    margin: 0;
    padding: 0;
    width: 859px;
    height: 1200px;
    overflow: hidden;
    background: var(--tag-red);
  }
  .swing-tag {
    display: block;
    width: 859px;
    height: 1200px;
  }
  .headline {
    font-family: "Anton", "Oswald", sans-serif;
    fill: var(--white);
  }
  .discount-figure {
    font-family: "Oswald", "Anton", sans-serif;
    font-weight: 700;
    fill: var(--figure-red);
  }
  .discount-word {
    font-family: "Montserrat", sans-serif;
    font-weight: 700;
    fill: var(--figure-red);
  }
  .shop-name {
    font-family: "Montserrat", sans-serif;
    font-weight: 400;
    fill: var(--white);
  }
</style>
</head>
<body>
<svg class="swing-tag" viewBox="0 0 859 1200" xmlns="http://www.w3.org/2000/svg">
  <defs>
    <radialGradient id="background-tone" cx="50%" cy="45%" r="70%">
      <stop offset="0" stop-color="#c8182e"/>
      <stop offset="1" stop-color="#b8112a"/>
    </radialGradient>
    <linearGradient id="ring-tone" x1="0" y1="0" x2="0" y2="1">
      <stop offset="0" stop-color="var(--ring-red)"/>
      <stop offset="0.55" stop-color="#c82030"/>
      <stop offset="1" stop-color="var(--ring-red-dark)"/>
    </linearGradient>
    <linearGradient id="disc-tone" x1="0" y1="0" x2="0" y2="1">
      <stop offset="0" stop-color="#ffffff"/>
      <stop offset="0.6" stop-color="#eeeeee"/>
      <stop offset="1" stop-color="var(--disc-shade)"/>
    </linearGradient>
    <radialGradient id="face-tone" cx="45%" cy="30%" r="75%">
      <stop offset="0" stop-color="#ffffff"/>
      <stop offset="0.7" stop-color="#f1f1f1"/>
      <stop offset="1" stop-color="#cfd3cf"/>
    </radialGradient>
    <filter id="disc-shadow" x="-20%" y="-20%" width="140%" height="140%">
      <feDropShadow dx="0" dy="4" stdDeviation="8" flood-color="#4a0008" flood-opacity="0.45"/>
    </filter>
  </defs>

  <rect class="background-pattern" role="img" aria-label="Red geometric diamond pattern background"
        x="0" y="0" width="859" height="1200" fill="url(#background-tone)"/>

  <rect class="frame-outer" x="12" y="12" width="835" height="1176" fill="none" stroke="var(--frame-blue)" stroke-width="1.2"/>
  <rect class="frame-inner" x="24" y="24" width="811" height="1152" fill="none" stroke="var(--frame-green)" stroke-width="1.2"/>

  <text class="headline" x="76" y="315" font-size="232" textLength="701" lengthAdjust="spacingAndGlyphs">REDUCED</text>

  <g class="discount-badge">
    <circle cx="429" cy="592" r="312" fill="url(#disc-tone)" filter="url(#disc-shadow)"/>
    <circle cx="429" cy="590" r="286" fill="url(#ring-tone)"/>
    <circle cx="429" cy="588" r="262" fill="#ffffff"/>
    <circle cx="431" cy="590" r="252" fill="url(#face-tone)"/>
    <text class="discount-figure" x="245" y="630" font-size="262" textLength="368" lengthAdjust="spacingAndGlyphs">20%</text>
    <text class="discount-word" x="310" y="765" font-size="138" textLength="240" lengthAdjust="spacingAndGlyphs">OFF</text>
  </g>

  <rect class="shop-mark" x="352" y="936" width="153" height="119" fill="none" stroke="var(--white)" stroke-width="1.2"/>
  <text class="shop-name" x="429.5" y="1106" font-size="36" text-anchor="middle" textLength="540" lengthAdjust="spacing">HOLLOWBROOK EMPORIUM</text>
</svg>
</body>
</html>
```